Spiritual journeyer, astrologer, Reiki master, underground music lover needs business card design

Initially I need a business card design (and possibly a logo for my new website). I offer astrological and energetic inquiry and guidance to clients in support of their life's evolutionary path. I combine an eclectic mix of methods with a focus on the mind body connection. I am a spiritual journeyer, astrologer, Reiki Master, certified personal trainer, soon to be black belt in Taekwondo (karate), and researcher into the benefits of music/sound vibrational therapy. And underground music lover :) The attached drawing is just something I drew freehand, it is symbolic of many things important to me. I wanted the figure to clearly be female. Her arms are open to catch the sky, the name of my new business is Orlabrook, and Orla is my daughter's name. This was just an idea I had, I'm open to suggestions. The photo is me with the planets in the sky as they were at the moment I was born (some years ago-LOL)
Updates

I have picked a final design. Thank you everyone for your time and effort.

Target Market(s)

Worldwide, what I do can be done in person or anywhere in the world via Skype

Industry/Entity Type

Professional Service

Contact Information for Business Card

Simple, unusual image with my business name and contact info

Font styles to use
Sans Serif

Requirements
Must have
• My website very clean, simple. Somehow combine biz name of Orlabrook with female figure catching/holding the starry sky? See my poor drawing I attached.
Nice to have
• Something that conveys all the unique, unusual, eclectic skills and capacities I have
Should not have
• Frilly, fancy, stuffy

```html
<!DOCTYPE html>
<html lang="en">
<head>
<meta charset="utf-8">
<title>Orlabrook Business Card</title>
<link href="https://fonts.googleapis.com/css2?family=Open+Sans:wght@400;600;700&display=swap" rel="stylesheet">
<style>
  :root {
    --page-bg: #e4e2df;
    --card-black: #161616;
    --ink-white: #ffffff;
    --ink-soft: #e8e8e8;
    --accent-orange: #f07d1a;
    --divider: #5a5a5a;
    --photo-red: #c8262a;
    --photo-cream: #efe9e1;
    --photo-wood: #9a6a3c;
    --mark-dark: #2a2a2a;
  }
  * { box-sizing: border-box; margin: 0; padding: 0; }
  html, body { width: 1200px; height: 814px; overflow: hidden; }
  body {
    background: var(--page-bg);
    font-family: "Open Sans", Arial, sans-serif;
    display: flex;
    align-items: center;
    justify-content: center;
    gap: 40px;
  }
  .card {
    width: 540px;
    height: 309px;
    position: relative;
    overflow: hidden;
    box-shadow: 0 6px 18px rgba(0,0,0,0.18);
  }
  /* Front */
  .card-front { background: var(--card-black); color: var(--ink-white); }
  .brand {
    position: absolute;
    left: 30px; top: 0; width: 215px; height: 100%;
    display: flex; flex-direction: column; align-items: center; justify-content: center;
    gap: 18px;
  }
  .brand-dot {
    width: 96px; height: 96px; border-radius: 50%;
    background: var(--accent-orange);
  }
  .brand-name {
    font-weight: 700; font-size: 27px; letter-spacing: 0.5px; color: var(--ink-white);
  }
  .divider {
    position: absolute; left: 262px; top: 40px; width: 1px; height: 230px;
    background: var(--divider);
  }
  .details { position: absolute; left: 284px; top: 52px; width: 240px; }
  .person-name { font-weight: 700; font-size: 19px; line-height: 1.2; margin-bottom: 4px; }
  .roles { color: var(--accent-orange); font-size: 14px; line-height: 1.3; margin-bottom: 12px; font-weight: 600; }
  .service { color: var(--ink-soft); font-size: 13.5px; line-height: 1.3; margin-bottom: 8px; }
  .contacts { list-style: none; font-size: 13.5px; color: var(--ink-soft); }
  .contacts li { display: flex; align-items: center; gap: 8px; line-height: 1.45; }
  .contacts svg { width: 12px; height: 12px; flex: none; fill: var(--accent-orange); }
  /* Back */
  .card-back { background: var(--photo-cream); }
  .portrait-scene {
    position: absolute; inset: 0;
    background:
      linear-gradient(180deg, var(--photo-red) 0%, var(--photo-red) 34%, var(--photo-cream) 36%, var(--photo-cream) 68%, var(--photo-wood) 100%);
  }
  .back-mark {
    position: absolute; right: 24px; top: 110px;
    display: flex; align-items: center; gap: 10px;
  }
  .back-mark .brand-dot { width: 54px; height: 54px; background: var(--mark-dark); }
  .back-mark .brand-name { color: var(--mark-dark); font-size: 24px; }
</style>
</head>
<body>
  <section class="card card-front">
    <div class="brand">
      <div class="brand-dot"></div>
      <div class="brand-name">ORLABROOK</div>
    </div>
    <div class="divider"></div>
    <div class="details">
      <p class="person-name">Maren Holloway</p>
      <p class="roles">Spiritual journeyer<br>Astrologer, Reiki Master<br>Certified personal trainer</p>
      <p class="service">Astrological and Energetic<br>Guidance and Inquery</p>
      <ul class="contacts">
        <li><svg viewBox="0 0 12 12"><path d="M2.4 0.6 4.2 2.8 3.2 4.2C3.8 5.6 5 6.9 6.6 7.8L8 6.8 10.4 8.6 9.4 11C5 11 0.8 6.8 1 2.4Z"/></svg>555-301-7284</li>
        <li><svg viewBox="0 0 12 12"><path d="M0 2H12V10H0ZM1 3 6 6.6 11 3V2.6H1Z"/></svg>email@orlabrook.com</li>
        <li><svg viewBox="0 0 12 12"><circle cx="6" cy="6" r="6"/></svg>www.orlabrook.com</li>
      </ul>
    </div>
  </section>

  <section class="card card-back">
    <div class="portrait-scene" role="img" aria-label="Photo of the astrologer seated on the floor of her red and white treatment room beside a massage table"></div>
    <div class="back-mark">
      <div class="brand-dot"></div>
      <div class="brand-name">ORLABROOK</div>
    </div>
  </section>
</body>
</html>
```